6' Banner Stands for exhibiting to Health Fairs with an audience of age 55+

We need designs for two 6' banner stands to stand on either side of our exhibition tables. We offer Hereditary Cancer Screening. I want the banners to have the same look and feel as the logo and the files color scheme logo, etc..

The Banners should have "Hereditary Cancer Screening" at the top with the Tag Line "The Test You Take For Them" underneath. A photo of grandparents with kids/grandkids and underneath the photos in large font one of the following messages:
1) "A Simple Swab Could Save A Family Members LIFE Get Tested Today!"
2) "Does Cancer Run In Your Family? Get Tested Today!"
3) "Knowledge Is Power" "Get Tested Today!"
4) "Will You Give Your Loved Ones The Information To Beat Cancer In Their Lives? Get Tested Today!
5) Knowledge Is Power Get Tested Today!"
Updates

Thank you all for your designs I now have the exact specs for the banners, so please use these as you update your designs. 31.5 inches X 83.25 inches and add a 1/2 inch bleed to all 4 sides. Thank you.

Target Market(s)

Persons 55+ who are grandparents

Industry/Entity Type

Healthcare

Font styles to use
Sans Serif
Other font styles liked:
• Comic Sans for "The Test You Take For Them"

Colors
9bcb3c
0356a4
ffffff

Requirements
Must have
• the main focus should be the hereditary cancer screening; "Hereditary Cancer Screening";
• "The test you order for them" in Comic Sans font underneath
• A photo or photos of grandparents with their grandchildren (multiple ethnicities)
• One of the slogans listed above
• GET TESTED TODAY underneath the messages at the bottom of the banner highlighted and eye catching
• www.kinwellpanel.example
Nice to have
• Logo at the top or bottom

```html
<!DOCTYPE html>
<html lang="en">
<head>
<meta charset="utf-8">
<title>Hereditary Cancer Screening – Banner Stands</title>
<link rel="stylesheet" href="https://fonts.googleapis.com/css2?family=Noto+Serif:wght@700&family=Comic+Neue:wght@400;700&family=Oswald:wght@500;700&family=Open+Sans:wght@400&display=swap">
<style>
  :root{
    --sheet:#8c8c8c;
    --green:#8dc63f;
    --navy:#232350;
    --white:#ffffff;
    --ink:#1c1c1c;
  }
  *{box-sizing:border-box;margin:0;padding:0}
  html,body{width:1200px;height:703px;overflow:hidden;background:var(--sheet)}
  .sheet{position:relative;width:1200px;height:703px}
  .label{position:absolute;font:400 9px "Open Sans",sans-serif;color:#222;letter-spacing:.3px}
  .banner{position:absolute;width:262px;height:605px;background:var(--white);overflow:hidden}
  .stripe-green{position:absolute;left:0;top:0;width:202px;height:10px;background:var(--green)}
  .stripe-navy{position:absolute;left:209px;top:0;width:53px;height:10px;background:var(--navy)}
  .title{position:absolute;left:0;width:100%;text-align:center;font:700 26px/26px "Noto Serif",serif;color:var(--navy);letter-spacing:.2px}
  .tagline{position:absolute;left:0;width:100%;text-align:center;font:400 16px "Comic Neue",sans-serif;color:var(--green)}
  .photo{position:absolute}
  .panel{position:absolute;left:0;width:100%;background:var(--navy);color:var(--white)}
  .slogan{font-family:"Comic Neue",sans-serif;font-weight:700;text-align:center}
  .accent{color:var(--green)}
  .cta{position:absolute;background:var(--green);border-radius:14px;color:var(--navy);font:700 22px "Comic Neue",sans-serif;display:flex;align-items:center;justify-content:center;letter-spacing:-.3px;box-shadow:0 6px 5px -3px rgba(0,0,0,.35);border:2px solid #a6d760}
  .footer{position:absolute;left:0;bottom:0;width:100%;height:45px;background:var(--navy);display:flex;align-items:center;justify-content:center;font:400 12px "Open Sans",sans-serif;color:var(--green)}
  .bold-line{position:absolute;left:0;width:100%;text-align:center;font-family:"Oswald",sans-serif;font-weight:700;color:var(--ink);text-transform:uppercase;line-height:1}
  .bold-line.accent,.bold-line .accent{color:var(--green)}
  .brand{position:absolute;left:0;width:100%;text-align:center;font:700 15px/15px "Comic Neue",sans-serif;color:var(--navy)}
</style>
</head>
<body>
<div class="sheet">

  <!-- Banner 1 -->
  <div class="label" style="left:42px;top:43px">BANNER 1</div>
  <section class="banner" style="left:42px;top:64px">
    <div class="stripe-green"></div><div class="stripe-navy"></div>
    <h1 class="title" style="top:43px">Herediatary<br>Cancer Screening</h1>
    <p class="tagline" style="top:112px">The Test You Take For Them</p>
    <div class="photo" role="img" aria-label="Photo of grandparents, parents and grandchildren together outdoors" style="left:0;top:167px;width:262px;height:171px;background:linear-gradient(160deg,#9fb78a,#c9d7e4 45%,#a8bfd8)"></div>
    <div class="panel slogan" style="top:345px;height:123px;padding-top:18px;font-size:27px;line-height:34px">DOES <span class="accent">CANCER</span> Run<br>in Your <span class="accent">Family?</span></div>
    <div class="cta" style="left:20px;top:450px;width:232px;height:58px;font-size:24px">Get Tested TODAY!</div>
    <div class="footer">www.kinwellpanel.example</div>
  </section>

  <!-- Banner 2 -->
  <div class="label" style="left:327px;top:45px">BANNER 2</div>
  <section class="banner" style="left:324px;top:60px">
    <div class="stripe-green"></div><div class="stripe-navy"></div>
    <h1 class="title" style="top:47px">Herediatary<br>Cancer Screening</h1>
    <p class="tagline" style="top:116px">The Test You Take For Them</p>
    <div class="panel slogan" style="top:170px;height:127px;padding-top:27px;font-size:24px;line-height:25px;font-weight:400">A Simple <b class="accent">Swab</b><br>Could <b class="accent">SAVE</b> A Family<br>Members <b class="accent">LIFE</b></div>
    <div class="photo" role="img" aria-label="Photo of smiling grandparents with two grandchildren in a garden" style="left:0;top:300px;width:262px;height:216px;background:linear-gradient(170deg,#7d9a63,#d9c2c2 55%,#e4d6cc)"></div>
    <div class="cta" style="left:30px;top:498px;width:206px;height:50px;font-size:21px">Get Tested TODAY!</div>
    <div class="footer">www.kinwellpanel.example</div>
  </section>

  <!-- Banner 3 -->
  <div class="label" style="left:609px;top:43px">BANNER 3</div>
  <section class="banner" style="left:609px;top:60px">
    <div class="stripe-green"></div><div class="stripe-navy"></div>
    <h1 class="title" style="top:34px">Herediatary<br>Cancer Screening</h1>
    <p class="tagline" style="top:96px">The Test You Take For Them</p>
    <div class="photo" role="img" aria-label="Photo of a laughing grandmother and grandfather with two young grandchildren" style="left:0;top:134px;width:262px;height:176px;background:linear-gradient(150deg,#cfc1b2,#e9b7cf 50%,#a9c4dd)"></div>
    <div class="bold-line" style="top:327px;font-size:26px;font-weight:500">Will you <span class="accent" style="font-size:34px;font-weight:700">Give</span></div>
    <div class="bold-line" style="top:360px;font-size:22px;font-weight:500">Your loved ones</div>
    <div class="bold-line" style="top:384px;left:47px;width:167px;height:19px;background:var(--navy);color:var(--white);font-size:15px;font-weight:500;padding-top:2px">The information to beat</div>
    <div class="bold-line accent" style="top:402px;font-size:52px">Cancer</div>
    <div class="bold-line" style="top:455px;font-size:22px;font-weight:500">In their lives ?</div>
    <div class="cta" style="left:46px;top:498px;width:165px;height:40px;font-size:18px">Get Tested TODAY!</div>
    <div class="footer">www.kinwellpanel.example</div>
  </section>

  <!-- Banner 4 -->
  <div class="label" style="left:889px;top:43px">BANNER 4</div>
  <section class="banner" style="left:889px;top:60px">
    <div class="stripe-green"></div><div class="stripe-navy"></div>
    <h1 class="title" style="top:47px">Herediatary<br>Cancer Screening</h1>
    <p class="tagline" style="top:116px">The Test You Take For Them</p>
    <div class="photo" role="img" aria-label="Photo of a grandmother hugging her granddaughter" style="left:0;top:170px;width:123px;height:122px;background:linear-gradient(160deg,#6e7a52,#c99f86 55%,#e3b3b8)"></div>
    <div class="photo" role="img" aria-label="Photo of three generations of a family smiling together" style="left:127px;top:170px;width:135px;height:122px;background:linear-gradient(160deg,#4f7a6a,#d89a84 50%,#c9574f)"></div>
    <div class="panel" style="top:298px;height:162px">
      <p class="slogan" style="position:absolute;left:12px;top:12px;font-size:23px;font-weight:400;text-align:left">knowing is better than</p>
      <p class="slogan" style="position:absolute;right:18px;top:40px;font-size:23px;font-weight:400">not knowing.</p>
      <svg style="position:absolute;left:11px;top:58px" width="66" height="76" viewBox="0 0 66 76" aria-hidden="true">
        <g fill="none" stroke="#8dc63f" stroke-width="3" stroke-linecap="round">
          <path d="M33 18c-11 0-18 8-18 17 0 7 5 11 7 15 1 2 1 5 1 7h20c0-2 0-5 1-7 2-4 7-8 7-15 0-9-7-17-18-17z"/>
          <path d="M25 62h16M26 67h14M29 72h8"/>
          <path d="M33 3v7M12 11l5 5M54 11l-5 5M2 33h7M57 33h7M8 54l5-4M58 54l-5-4"/>
        </g>
      </svg>
      <p class="slogan accent" style="position:absolute;left:93px;top:86px;font-size:25px;font-weight:400">Knowledge</p>
      <p class="slogan accent" style="position:absolute;right:20px;top:114px;font-size:32px;font-weight:400">is Power</p>
    </div>
    <div class="cta" style="left:31px;top:450px;width:198px;height:50px;font-size:21px">Get Tested TODAY!</div>
    <p class="brand" style="top:523px">Kinwell Care</p>
    <div class="footer">www.kinwellpanel.example</div>
  </section>

</div>
</body>
</html>
```